Brightvale Copackaging Website using Wix Platform

Project Overview:
Brightvale Copackaging is a supply chain company specializing in packaging and manufacturing services for CPG (Consumer Packaged Goods) brands and nutritional/dietary supplement companies. The company offers end-to-end solutions including packaging design, production, co-packing, and private labeling. The goal of this project is to create a professional, user-friendly website that showcases your expertise, builds trust with potential clients, and generates leads for your services.

Objectives:
Establish Brand Authority: Position Brightvale Copackaging as a leader in the packaging and manufacturing industry for CPG and nutritional products.
Lead Generation: Encourage visitors to contact you for quotes, consultations, or further information.
Professional User Experience: Ensure the website is easy to navigate, visually appealing, and mobile-friendly.
SEO & Conversion Optimization: Optimize the site for search engines to attract organic traffic and improve conversion rates.
Primary Audience:
CPG Brands: Companies in industries like food and beverage, personal care, and household products looking for packaging and manufacturing services.
Nutritional/Dietary Supplement Brands: Companies in the health and wellness industry needing specialized packaging and manufacturing services for supplements, including compliance with regulatory standards (GMP).
Secondary Audience:
Potential partners looking to collaborate on co-packing or private labeling.
Key Features & Functionality:
Responsive Design:

The website must be fully responsive, ensuring optimal viewing across all devices (desktops, tablets, mobile).
User-Centric Navigation:

A clean, intuitive navigation system that allows users to quickly access key pages such as Home, Services, About Us, Case Studies, FAQ, and Contact.
Lead Generation Forms:

Prominent CTAs (Calls to Action) throughout the website encouraging users to “Request a Quote”, “Get in Touch”, or “Learn More” about your services.
Contact Form: Simple form allowing potential clients to submit inquiries about your services.
SEO Optimization:

The site should be optimized for relevant keywords (e.g., “co-packing services for CPG,” “nutritional supplement packaging,” “custom packaging solutions”), including meta descriptions, headers, and on-page content.
Content Management System (CMS):

An easy-to-use CMS (like WordPress or Webflow) for easy content updates. This will allow you to make changes to your services, case studies, and other sections without requiring a developer.
Analytics Integration:

Google Analytics or a similar tool for tracking site visitors and performance metrics to make data-driven decisions on site improvements.
Site Structure & Content:
1. Home Page:
Hero Section with tagline, images or video of your services in action, and a clear CTA (e.g., “Request a Quote”).
Value Proposition: Short and compelling introduction to Brightvale Copackaging’s core services and advantages.
Overview of Services: Highlight your key offerings (e.g., Packaging Design, Co-packing, Nutritional Supplement Packaging, Private Labeling).
Client Logos/Testimonials: Social proof to establish credibility.
CTA Buttons: Throughout the page to drive conversions (e.g., “Get a Free Consultation”).
2. About Us Page:
Company Overview: Explain your mission, values, and commitment to quality.
Team Overview (Optional): Introduce key team members to humanize your company and build trust.
Core Values and Differentiators: Showcase what makes Brightvale Copackaging unique—sustainability practices, regulatory compliance, and industry expertise.
3. Services Pages (Separate Pages for Each Service):
Packaging & Design: Custom packaging solutions, materials, and design services for CPG brands.
Manufacturing & Assembly: Your end-to-end production process, assembly capabilities, and how you support both small and large-scale runs.
Nutritional & Dietary Supplement Packaging: Focus on specialized packaging for supplements, regulatory compliance (GMP), and certifications.
Private Labeling: Services for clients who wish to brand their own products using your packaging.
Each service page will include detailed descriptions, benefits, process information, and CTAs like “Get Started” or “Request a Quote”.
4. Case Studies / Portfolio Page:
Success Stories: Showcase in-depth case studies of past projects, especially successful partnerships with CPG or supplement brands.
Before & After Images: Display the difference your services have made for clients, especially in terms of packaging quality or branding improvements.
Client Testimonials: Additional customer feedback to strengthen your brand reputation.
5. FAQ Page:
Address common questions related to lead times, regulatory compliance, order quantities, and specific details for different industries (e.g., dietary supplements).
The format will be accordion-style or dropdowns for easy scanning.
6. Contact Us Page:
Contact Form: With fields for name, email, company, and inquiry details.
Location Information: Physical address, phone number, and working hours.
Map Integration: If relevant, integrate Google Maps to show your office location.
Social Media Links: Link to your company’s LinkedIn, Instagram, or other relevant platforms.

Target Market(s)

Startup CPG Brands, Supplement Brands, Nutrition Brands

Industry/Entity Type

Flexible Packaging, Contract Manufacturing, Supplement & Food Manufacturing

Requirements
Must have
• Use our colors.
Nice to have
• https://example-site.net/brightvalecopackaging - www.tarnwick.com - www.plumrossfoods.com - thebluegarner.co

```html
<!DOCTYPE html>
<html lang="en">
<head>
<meta charset="utf-8">
<title>Brightvale Copackaging</title>
<link href="https://fonts.googleapis.com/css2?family=Poppins:ital,wght@0,400;0,500;0,600;0,700;1,400&display=swap" rel="stylesheet">
<style>
:root{
  --navy:#22223f;
  --blue:#1f66a8;
  --green:#8ce04e;
  --ink:#222;
  --text:#444;
  --hero-bg:#ececec;
  --white:#fff;
}
*{box-sizing:border-box;margin:0;padding:0}
html,body{width:1200px;height:4938px;overflow:hidden}
body{position:relative;font-family:'Poppins',sans-serif;color:var(--ink);background:var(--white)}
.abs{position:absolute}
.btn{position:absolute;display:flex;align-items:center;justify-content:center;gap:10px;background:var(--blue);color:var(--white);font-size:15px;font-weight:500;text-transform:uppercase;letter-spacing:.2px}
.btn .dot{width:17px;height:17px;border-radius:50%;background:var(--white);display:flex;align-items:center;justify-content:center}
.photo{position:absolute}
.underline{position:absolute;height:4px;width:70px;background:var(--green)}
.site-header{position:absolute;left:0;top:0;width:1200px;height:100px;background:var(--navy)}
.brand{position:absolute;color:var(--white);font-size:21px;font-weight:400;letter-spacing:.5px;display:flex;align-items:center;gap:10px;text-transform:uppercase}
.brand .mark{width:16px;height:16px;background:var(--green)}
.main-nav{position:absolute;right:68px;top:0;height:100px;display:flex;align-items:center;gap:30px;color:var(--white);font-size:13px;text-transform:uppercase}
.hero{position:absolute;left:0;top:100px;width:1200px;height:594px;background:var(--hero-bg)}
.hero h1{position:absolute;left:67px;top:107px;font-size:47px;line-height:58px;font-weight:600;text-transform:uppercase;color:var(--ink)}
.hero p{position:absolute;left:67px;top:258px;width:590px;font-size:15.5px;line-height:27px;color:var(--ink)}
.section-title{position:absolute;left:0;width:1200px;text-align:center;font-size:47px;font-weight:600;text-transform:uppercase}
.svc-card{position:absolute;width:522px;height:453px;background:var(--white);box-shadow:0 0 12px rgba(0,0,0,.15)}
.svc-card .photo{left:6px;top:10px;width:510px;height:219px}
.svc-card h3{position:absolute;left:0;top:262px;width:100%;text-align:center;font-size:22px;font-weight:500;text-transform:uppercase}
.svc-card .underline{left:236px;top:298px;width:50px;height:3px}
.svc-card p{position:absolute;left:40px;top:313px;width:442px;text-align:center;font-size:14px;line-height:27px;color:var(--text)}
.svc-card .btn{left:189px;top:378px;width:144px;height:35px;font-size:14px}
.t-card{position:absolute;top:3405px;width:252px;height:333px;background:var(--white);box-shadow:0 0 12px rgba(0,0,0,.14)}
.t-card .quote{position:absolute;left:0;top:10px;width:100%;text-align:center;font-size:110px;line-height:110px;color:#dedede;font-weight:700;font-style:normal}
.t-card p{position:absolute;left:20px;top:104px;width:212px;font-size:13.5px;line-height:25px;font-style:italic;text-align:justify;color:var(--text)}
.t-card .avatar{position:absolute;left:38px;top:253px;width:48px;height:48px;border-radius:50%;background:linear-gradient(#c9c9c9,#8c8c8c)}
.t-card .who{position:absolute;left:98px;top:252px;font-size:14px;line-height:17px}
.t-card .who b{display:block;color:var(--blue);font-weight:500}
.t-card .who span{display:block;font-size:11px;font-weight:500}
.t-card .who i{display:block;font-style:normal;font-size:10px;color:#e8b400;letter-spacing:1px}
.arrow{position:absolute;top:3530px;width:52px;height:52px;border-radius:50%;display:flex;align-items:center;justify-content:center}
.field{position:absolute;background:var(--white);font-size:11px;color:#999;padding:12px 18px}
.f-contact{position:absolute;top:4726px;display:flex;gap:14px;color:var(--white);font-size:13.5px;line-height:19px}
.f-contact .ico{width:22px;height:22px;border-radius:4px;background:var(--blue);margin-top:4px;display:flex;align-items:center;justify-content:center}
.footer-nav span{position:absolute;top:4833px;color:var(--white);font-size:14px;text-transform:uppercase}
</style>
</head>
<body>

<header class="site-header">
  <div class="brand" style="left:67px;top:37px"><span class="mark"></span>Brightvale Copackaging</div>
  <nav class="main-nav"><span>Home</span><span>Services</span><span>About Us</span><span>Case Studies</span><span>FAQ</span><span>Contact</span></nav>
</header>

<section class="hero">
  <h1>Ready to Transform<br>Your Packaging?</h1>
  <p>Our comprehensive range of packaging options includes high-quality labels, versatile flexible packaging, custom shrink sleeves, and premium display folding cartons—all designed to meet your unique needs and exceed industry standards..</p>
  <div class="btn" style="left:67px;top:398px;width:198px;height:58px">Request a Quote <span class="dot"><svg width="8" height="8" viewBox="0 0 8 8"><path d="M2 1l3 3-3 3" stroke="#1f66a8" stroke-width="1.6" fill="none"/></svg></span></div>
  <div class="photo" role="img" aria-label="Stacked cardboard boxes on the floor" style="left:330px;top:420px;width:390px;height:174px;background:linear-gradient(#d8b888,#b38a58);opacity:.8"></div>
  <div class="photo" role="img" aria-label="Smiling worker in overalls carrying cardboard boxes" style="left:660px;top:80px;width:540px;height:514px;background:radial-gradient(ellipse at 55% 50%,#c9a87c 0%,#9a8570 40%,#3f5a86 75%,#e6e6e6 100%)"></div>
</section>

<section aria-label="About us">
  <div class="abs" style="left:0;top:694px;width:426px;height:625px;background:var(--blue)"></div>
  <div class="photo" role="img" aria-label="Two managers reviewing plans inside a packaging warehouse" style="left:67px;top:782px;width:663px;height:441px;background:linear-gradient(135deg,#9aa0a0,#6e6860 50%,#b9a070)"></div>
  <h2 class="abs" style="left:776px;top:840px;font-size:47px;font-weight:600;text-transform:uppercase">About Us</h2>
  <div class="underline" style="left:776px;top:906px;width:64px"></div>
  <p class="abs" style="left:776px;top:934px;width:358px;font-size:13px;line-height:27px;color:var(--text);text-align:justify">Brightvale Copackaging is a family-owned business in Varnholt, Ohio, with extensive experience in manufacturing and regulatory compliance. We simplify the manufacturing process with step-by-step guidance and a friendly customer service team. Let's take brand to the next level!</p>
  <div class="btn" style="left:776px;top:1131px;width:158px;height:50px">Learn More <span class="dot"><svg width="8" height="8" viewBox="0 0 8 8"><path d="M2 1l3 3-3 3" stroke="#1f66a8" stroke-width="1.6" fill="none"/></svg></span></div>
</section>

<section aria-label="Our services">
  <h2 class="section-title" style="top:1415px">Our Services</h2>
  <div class="underline" style="left:565px;top:1484px"></div>
  <p class="abs" style="left:140px;top:1541px;width:920px;text-align:center;font-size:14.5px;line-height:27px;color:var(--text)">Lorem ipsum dolor sit amet, consectetur adipiscing elit. Sed pharetra, turpis vitae tincidunt tempus, ipsum magna varius mauris, et dictum nulla neque ac turpis. Etiam finibus est metus, eu viverra velit auctor ac.</p>

  <article class="svc-card" style="left:67px;top:1652px">
    <div class="photo" role="img" aria-label="Juice bottles and kraft gift boxes with green bands" style="background:linear-gradient(90deg,#8a4a2c,#c8a27a 45%,#e4d6c4)"></div>
    <h3>Packaging Design</h3><div class="underline"></div>
    <p>Lorem ipsum dolor sit amet, consectetur adipiscing elit. Morbi vitae velit ac velit vulputate placerat commodo at mauris.</p>
    <div class="btn">Read More</div>
  </article>
  <article class="svc-card" style="left:613px;top:1652px">
    <div class="photo" role="img" aria-label="Hands sealing a cardboard box with a tape dispenser" style="background:linear-gradient(90deg,#6d5a48,#c8b49e 50%,#8a6a4e)"></div>
    <h3>Co-Packing</h3><div class="underline"></div>
    <p>Lorem ipsum dolor sit amet, consectetur adipiscing elit. Morbi vitae velit ac velit vulputate placerat commodo at mauris.</p>
    <div class="btn">Read More</div>
  </article>
  <article class="svc-card" style="left:67px;top:2153px">
    <div class="photo" role="img" aria-label="Rows of white supplement pouches" style="background:linear-gradient(90deg,#d6d4cf,#8c8880 50%,#e0ded8)"></div>
    <h3>Nutritional Supplement Packaging</h3><div class="underline"></div>
    <p>Lorem ipsum dolor sit amet, consectetur adipiscing elit. Morbi vitae velit ac velit vulputate placerat commodo at mauris</p>
    <div class="btn">Read More</div>
  </article>
  <article class="svc-card" style="left:613px;top:2153px">
    <div class="photo" role="img" aria-label="Person labeling a parcel with a tape gun" style="background:linear-gradient(90deg,#4a5a8a,#c8a888 55%,#c45a3a)"></div>
    <h3>Private Labeling</h3><div class="underline"></div>
    <p>Lorem ipsum dolor sit amet, consectetur adipiscing elit. Morbi vitae velit ac velit vulputate placerat commodo at mauris.</p>
    <div class="btn">Read More</div>
  </article>
</section>

<section aria-label="Consultation">
  <div class="abs" style="left:566px;top:2736px;width:634px;height:402px;background:var(--blue)"></div>
  <div class="photo" role="img" aria-label="Designer cutting printed packaging proofs on a desk" style="left:0;top:2736px;width:566px;height:402px;background:linear-gradient(135deg,#c9ccd0,#6f7278 50%,#d8d8d8)"></div>
  <h2 class="abs" style="left:644px;top:2782px;font-size:45px;line-height:56px;font-weight:600;color:var(--white);text-transform:uppercase">Packaging and<br>Manufacturing<br>Services are<br>Available Here</h2>
  <div class="btn" style="left:648px;top:3029px;width:295px;height:48px;background:var(--green);color:var(--blue)">Get a Free Consultation <span class="dot" style="background:var(--blue)"><svg width="8" height="8" viewBox="0 0 8 8"><path d="M2 1l3 3-3 3" stroke="#8ce04e" stroke-width="1.6" fill="none"/></svg></span></div>
</section>

<section aria-label="Client testimonials">
  <h2 class="section-title" style="top:3226px">Client Testimonials</h2>
  <div class="underline" style="left:565px;top:3296px"></div>
  <div class="arrow" style="left:9px;background:#c4c4c4"><svg width="10" height="12" viewBox="0 0 10 12"><path d="M7 2L3 6l4 4" stroke="#fff" stroke-width="2" fill="none"/></svg></div>
  <div class="arrow" style="left:1138px;background:var(--blue)"><svg width="10" height="12" viewBox="0 0 10 12"><path d="M3 2l4 4-4 4" stroke="#fff" stroke-width="2" fill="none"/></svg></div>
  <article class="t-card" style="left:67px"><div class="quote">”</div><p>Lorem ipsum dolor sit amet, consectetur adipiscing elit, sed do eiusmod tempor incididunt ut labore et dolore magna</p><div class="avatar" role="img" aria-label="Client portrait"></div><div class="who"><b>Marcus Ellery</b><span>CEO</span><i>★★★★★</i></div></article>
  <article class="t-card" style="left:335px"><div class="quote">”</div><p>Lorem ipsum dolor sit amet, consectetur adipiscing elit, sed do eiusmod tempor incididunt ut labore et dolore magna</p><div class="avatar" role="img" aria-label="Client portrait"></div><div class="who"><b>Marcus Ellery</b><span>CEO</span><i>★★★★★</i></div></article>
  <article class="t-card" style="left:606px"><div class="quote">”</div><p>Lorem ipsum dolor sit amet, consectetur adipiscing elit, sed do eiusmod tempor incididunt ut labore et dolore magna</p><div class="avatar" role="img" aria-label="Client portrait"></div><div class="who"><b>Marcus Ellery</b><span>CEO</span><i>★★★★★</i></div></article>
  <article class="t-card" style="left:876px"><div class="quote">”</div><p>Lorem ipsum dolor sit amet, consectetur adipiscing elit, sed do eiusmod tempor incididunt ut labore et dolore magna</p><div class="avatar" role="img" aria-label="Client portrait"></div><div class="who"><b>Marcus Ellery</b><span>CEO</span><i>★★★★★</i></div></article>
  <svg class="abs" style="left:540px;top:3805px" width="120" height="16" viewBox="0 0 120 16">
    <circle cx="11" cy="8" r="5" fill="#8ce04e"/>
    <circle cx="44" cy="8" r="5" fill="none" stroke="#8ce04e" stroke-width="1.5"/>
    <circle cx="77" cy="8" r="5" fill="none" stroke="#8ce04e" stroke-width="1.5"/>
    <circle cx="108" cy="8" r="5" fill="none" stroke="#8ce04e" stroke-width="1.5"/>
  </svg>
</section>

<section aria-label="Contact us">
  <div class="abs" style="left:0;top:3936px;width:1200px;height:1002px;background:var(--navy)"></div>
  <div class="abs" style="left:0;top:3936px;width:215px;height:636px;background:var(--green)"></div>
  <div class="photo" role="img" aria-label="Smiling woman working at a computer" style="left:73px;top:4054px;width:406px;height:451px;background:linear-gradient(90deg,#b88a6a,#e8e6e2 55%,#f2f2f2)"></div>
  <h2 class="abs" style="left:546px;top:4030px;font-size:45px;font-weight:600;color:var(--white);text-transform:uppercase">Contact Us</h2>
  <div class="underline" style="left:546px;top:4100px"></div>
  <p class="abs" style="left:546px;top:4134px;width:580px;font-size:12.5px;line-height:24px;color:var(--white)">If you have any questions or need help, please fill out the form below. We are here to help and answer any questions you might have. We look forward to hearing from you.</p>
  <div class="field" style="left:546px;top:4219px;width:549px;height:39px">Name:</div>
  <div class="field" style="left:546px;top:4279px;width:267px;height:40px">Phone:</div>
  <div class="field" style="left:826px;top:4279px;width:269px;height:40px">Email:</div>
  <div class="field" style="left:546px;top:4338px;width:549px;height:81px">Message:</div>
  <div class="btn" style="left:546px;top:4449px;width:156px;height:50px">Learn More <span class="dot"><svg width="8" height="8" viewBox="0 0 8 8"><path d="M2 1l3 3-3 3" stroke="#1f66a8" stroke-width="1.6" fill="none"/></svg></span></div>
</section>

<footer>
  <div class="brand" style="left:0;top:4640px;width:1200px;justify-content:center"><span class="mark"></span>Brightvale Copackaging</div>
  <div class="f-contact" style="left:238px"><span class="ico"><svg width="12" height="12" viewBox="0 0 12 12"><path d="M3 1l2 2-1 2 3 3 2-1 2 2-2 2C5 11 1 7 1 3z" fill="#8ce04e"/></svg></span><span>CALL US<br>8012 555 0147</span></div>
  <div class="f-contact" style="left:432px"><span class="ico"><svg width="12" height="10" viewBox="0 0 12 10"><rect x="1" y="1" width="10" height="8" fill="#8ce04e"/><path d="M1 1l5 4 5-4" stroke="#1f66a8" fill="none"/></svg></span><span>EMAIL US<br>info@brightvalepack.com</span></div>
  <div class="f-contact" style="left:690px"><span class="ico"><svg width="10" height="13" viewBox="0 0 10 13"><path d="M5 12S1 7 1 4.5a4 4 0 018 0C9 7 5 12 5 12z" fill="#8ce04e"/><circle cx="5" cy="4.5" r="1.5" fill="#1f66a8"/></svg></span><span>Address line Dummy Here<br>Address line Here</span></div>
  <div class="abs" style="left:67px;top:4806px;width:1066px;height:1px;background:rgba(255,255,255,.25)"></div>
  <nav class="footer-nav">
    <span style="left:210px">Home</span>
    <span style="left:327px">Services</span>
    <span style="left:471px">About Us</span>
    <span style="left:616px">Case Studies</span>
    <span style="left:792px">FAQ</span>
    <span style="left:896px">Contact Us</span>
  </nav>
  <div class="abs" style="left:0;top:4879px;width:1200px;height:59px;background:var(--blue)"></div>
  <p class="abs" style="left:67px;top:4913px;font-size:10px;color:var(--white)">Copyright © 2024 All Rights Reserved By Company name</p>
  <div class="abs" style="left:1012px;top:4898px;display:flex;gap:6px">
    <span style="width:26px;height:26px;border:1.5px solid #fff;border-radius:3px"></span>
    <span style="width:26px;height:26px;border:1.5px solid #fff;border-radius:3px"></span>
    <span style="width:26px;height:26px;border:1.5px solid #fff;border-radius:3px"></span>
    <span style="width:26px;height:26px;border:1.5px solid #fff;border-radius:3px"></span>
  </div>
</footer>

</body>
</html>
```